Thermostat Screen Design

We need a screen layout design for a new thermostat we're currently developing. If you're not familiar with thermostats, you can see some examples here - http://smart-climate-units-guide.bestpickdigest.com/

We're after the main page design, with icons, colours etc. It needs to be clean, modern and minimalistic. Attached is all components required on the screen. The screen size is 5 inch (diagnol).

The arrows on the screen showcase what happens when you press a button. For example, when you press MODE once you get OFF, press it twice, HEAT, press it 3 times, COOL, etc. This is just for your reference.

You have complete creative license on how you choose to layout the screen, position the components etc, but we require:

- it must be on a 5 inch screen diagnol
- modern, clean and minimalistic
- includes icons and colours
- Intuitive

Let me know if any questions.

```html
<!DOCTYPE html>
<html lang="en">
<head>
<meta charset="utf-8">
<title>Thermostat Screen Design</title>
<link rel="stylesheet" href="https://fonts.googleapis.com/css2?family=Open+Sans:wght@300;400&display=swap">
<style>
  :root {
    --page-bg: #e8e4de;
    --status-bar: #3b3430;
    --photo-dark: #5a2410;
    --photo-mid: #a4451c;
    --photo-warm: #c5622a;
    --photo-light: #d9895a;
    --nav-top: #1c1613;
    --nav-bottom: #050505;
    --nav-active: #000000;
    --text-light: #ffffff;
    --text-soft: #f1ece8;
  }
  * { margin: 0; padding: 0; box-sizing: border-box; }
  html, body {
    width: 1200px;
    height: 675px;
    overflow: hidden;
    background: var(--page-bg);
    font-family: "Open Sans", "Segoe UI", sans-serif;
  }
  .screen {
    position: absolute;
    left: 98px;
    top: 17px;
    width: 1004px;
    height: 640px;
    overflow: hidden;
    background: var(--photo-mid);
  }
  .backdrop {
    position: absolute;
    inset: 0;
    background:
      radial-gradient(ellipse 30% 25% at 88% 55%, rgba(40,40,40,0.55), transparent 70%),
      radial-gradient(ellipse 35% 30% at 25% 20%, var(--photo-light), transparent 70%),
      radial-gradient(ellipse 30% 35% at 12% 80%, var(--photo-dark), transparent 75%),
      linear-gradient(90deg, var(--photo-warm) 0%, var(--photo-mid) 45%, #8e3a18 70%, #6a3a28 100%);
  }
  .status-bar {
    position: absolute;
    left: 0; top: 0;
    width: 100%;
    height: 67px;
    background: var(--status-bar);
    color: var(--text-light);
    font-size: 22px;
    font-weight: 400;
  }
  .status-item {
    position: absolute;
    top: 50%;
    transform: translate(-50%, -50%);
    white-space: nowrap;
  }
  .reading {
    position: absolute;
    color: var(--text-light);
    text-align: center;
    transform: translateX(-50%);
  }
  .reading-label {
    display: block;
    font-size: 23px;
    font-weight: 400;
    color: var(--text-soft);
  }
  .reading-value {
    display: inline-block;
    position: relative;
    font-weight: 300;
    line-height: 1;
  }
  .reading-unit {
    position: absolute;
    left: 100%;
    top: 0;
    font-weight: 300;
    padding-left: 4px;
  }
  .room { left: 420px; top: 224px; }
  .room .reading-value { font-size: 190px; margin-top: -4px; letter-spacing: -6px; }
  .room .reading-unit { font-size: 40px; top: 10px; }
  .outdoor { left: 826px; top: 88px; }
  .outdoor .reading-value { font-size: 96px; letter-spacing: -2px; }
  .outdoor .reading-unit { font-size: 24px; top: 2px; }
  .nav-bar {
    position: absolute;
    left: 0; bottom: 0;
    width: 100%;
    height: 95px;
    background: linear-gradient(180deg, var(--nav-top) 0, var(--nav-top) 38px, var(--nav-bottom) 38px);
    color: var(--text-light);
    font-size: 22px;
  }
  .nav-active {
    position: absolute;
    left: 0; top: 0;
    width: 232px;
    height: 100%;
    background: linear-gradient(180deg, rgba(0,0,0,0.5) 0, rgba(0,0,0,0.5) 38px, var(--nav-active) 38px);
  }
  .nav-item {
    position: absolute;
    top: 50%;
    transform: translate(-50%, -50%);
    letter-spacing: 0.5px;
  }
</style>
</head>
<body>
  <main class="screen">
    <div class="backdrop" role="img" aria-label="Blurred warm kitchen interior with a cat peeking up from the bottom edge"></div>

    <header class="status-bar">
      <span class="status-item" style="left:93px">12:14</span>
      <span class="status-item" style="left:301px">12/02/2014</span>
      <span class="status-item" style="left:480px">Wednesday</span>
      <span class="status-item" style="left:714px">Sleep</span>
      <span class="status-item" style="left:906px">Zone 02</span>
    </header>

    <section class="reading outdoor">
      <span class="reading-label">Outdoor Temperature</span>
      <span class="reading-value">22<span class="reading-unit">°C</span></span>
    </section>

    <section class="reading room">
      <span class="reading-label">Room Temperature</span>
      <span class="reading-value">18<span class="reading-unit">°C</span></span>
    </section>

    <nav class="nav-bar">
      <div class="nav-active"></div>
      <span class="nav-item" style="left:118px">MODE</span>
      <span class="nav-item" style="left:339px">FAN</span>
      <span class="nav-item" style="left:584px">SETTINGS</span>
      <span class="nav-item" style="left:872px">ZONES</span>
    </nav>
  </main>
</body>
</html>
```